New tech executive consulting company needs professionally branded document templates

We are a new business selling fractional board advisory and go-to-market consulting services into the Technology space. Partwise Helm are experts in providing high-quality executive-level leaders on a part-time basis to tech companies in need of their expertise. We work closely with clients to understand their business needs, challenges, and goals, and provides customised solutions to help them succeed. Due to our audience we need the design to have a high quality, executive look and feel.

Our first website is live and can be found at partwisehelm.tech. We also already have a logo which I've uploaded. Our brand is clean and uses orange to give it colour and an identity that stands out.

We need some document master templates created so we can create our own presentations (Google Slides & Powerpoint), PDF documents, and Word templates, and ideally also a LinkedIn banner.

```html
<!DOCTYPE html>
<html lang="en">
<head>
<meta charset="utf-8">
<title>Partwise Helm – Presentation Templates</title>
<link href="https://fonts.googleapis.com/css2?family=Open+Sans:wght@400;600;700;800&display=swap" rel="stylesheet">
<style>
:root{
  --orange:#ee834e;
  --orange-soft:#f09462;
  --navy:#2d3441;
  --ink:#3a3f47;
  --grey:#9a9a9a;
  --light:#f2f2f2;
  --canvas:#d9d9d9;
  --white:#ffffff;
}
*{box-sizing:border-box;margin:0;padding:0}
html,body{width:1200px;height:2431px;overflow:hidden}
body{background:var(--canvas);font-family:"Open Sans",Arial,sans-serif;color:var(--ink);position:relative}
.slide{position:absolute;width:540px;height:304px;background:var(--white);overflow:hidden}
.slide--hero{left:234px;top:111px;transform:scale(1.3556);transform-origin:0 0}
.photo{position:absolute}
.photo--meeting{background:linear-gradient(135deg,#dfe3e6 0%,#a9b3bd 40%,#3c4d5e 70%,#1e2a35 100%)}
.photo--towers{background:linear-gradient(160deg,#eef1f3 0%,#b8c4cc 40%,#46606c 75%,#1d2b31 100%)}
.photo--desk{background:linear-gradient(120deg,#7a6a5a 0%,#b9a68f 40%,#d8cfc4 70%,#eeeae4 100%)}
.photo--chart{background:linear-gradient(120deg,#f4f5f7 0%,#dfe4ea 60%,#b7c3d1 100%)}
.logo{position:absolute;font-weight:700;color:var(--navy);letter-spacing:.12em;text-align:center;line-height:1.05}
.logo--corner{right:20px;top:16px;font-size:8px}
.logo--large{font-size:15px}
.heading{position:absolute;left:22px;top:18px;display:flex;align-items:center;gap:6px;font-size:16px;color:var(--navy)}
.heading svg{width:18px;height:28px;flex:none}
.heading b{font-weight:700}
.footer{position:absolute;right:16px;bottom:14px;display:flex;align-items:center;gap:8px;font-size:4.3px;color:var(--navy)}
.footer b{font-weight:700}
.page{width:8px;height:8px;background:var(--orange);color:var(--white);font-size:4.5px;font-weight:700;display:flex;align-items:center;justify-content:center}
.lorem{font-size:5.2px;line-height:1.3;color:var(--navy)}
.circle{position:absolute;border-radius:50%;display:flex;align-items:center;justify-content:center}
.circle svg,.square svg{width:55%;height:55%}
.square{position:absolute;width:30px;height:30px;background:var(--orange);display:flex;align-items:center;justify-content:center}
.orange{color:var(--orange)}
</style>
</head>
<body>

<!-- Title slide, feature size -->
<section class="slide slide--hero" aria-label="Title slide">
  <div class="photo photo--meeting" role="img" aria-label="Photo of business people shaking hands over a tablet showing a stock chart" style="inset:0;clip-path:polygon(474px 0,540px 0,540px 304px,270px 304px)"></div>
  <svg style="position:absolute;inset:0" width="540" height="304"><polygon points="459,0 490,0 275,304 244,304" fill="#ee834e"/></svg>
  <div class="logo logo--large" style="left:48px;top:42px">PARTWISE<br>HELM</div>
  <h1 style="position:absolute;left:48px;top:124px;font-size:22px;font-weight:800;line-height:1.12;color:var(--orange)">PRESENTATION<br>TITLE GOES HERE!</h1>
  <p style="position:absolute;left:48px;top:184px;font-size:6.6px;line-height:1.25;color:var(--navy)">Lorem ipsum dolor sit amet, consectetur adipiscing elit.<br>Vivamus eu dui ex. Curabitur dapibus dignissim dui, in molestie.</p>
  <p style="position:absolute;left:48px;top:221px;font-size:5px;color:var(--navy)">Sunday, July 16, 2023</p>
  <p style="position:absolute;left:48px;top:268px;font-size:4.3px;color:var(--navy)">Copyright © 2023 <b>Partwise Helm</b>. All Rights Reserved.</p>
</section>

<!-- 1 Title -->
<section class="slide" style="left:51px;top:786px" aria-label="Title slide">
  <div class="photo photo--meeting" role="img" aria-label="Photo of business people shaking hands over a tablet showing a stock chart" style="inset:0;clip-path:polygon(474px 0,540px 0,540px 304px,270px 304px)"></div>
  <svg style="position:absolute;inset:0" width="540" height="304"><polygon points="459,0 490,0 275,304 244,304" fill="#ee834e"/></svg>
  <div class="logo logo--large" style="left:48px;top:42px">PARTWISE<br>HELM</div>
  <h1 style="position:absolute;left:48px;top:124px;font-size:22px;font-weight:800;line-height:1.12;color:var(--orange)">PRESENTATION<br>TITLE GOES HERE!</h1>
  <p style="position:absolute;left:48px;top:184px;font-size:6.6px;line-height:1.25;color:var(--navy)">Lorem ipsum dolor sit amet, consectetur adipiscing elit.<br>Vivamus eu dui ex. Curabitur dapibus dignissim dui, in molestie.</p>
  <p style="position:absolute;left:48px;top:221px;font-size:5px;color:var(--navy)">Sunday, July 16, 2023</p>
  <p style="position:absolute;left:48px;top:268px;font-size:4.3px;color:var(--navy)">Copyright © 2023 <b>Partwise Helm</b>. All Rights Reserved.</p>
</section>

<!-- 2 Bullets -->
<section class="slide" style="left:609px;top:786px" aria-label="Bullet list slide">
  <div class="photo photo--meeting" role="img" aria-label="Photo of a handshake across a meeting table" style="inset:0;clip-path:polygon(0 0,255px 0,40px 304px,0 304px)"></div>
  <svg style="position:absolute;inset:0" width="540" height="304"><polygon points="255,0 272,0 57,304 40,304" fill="#ee834e"/></svg>
  <div class="logo logo--corner">PARTWISE<br>HELM</div>
  <div class="heading" style="left:252px;top:72px"><svg viewBox="0 0 18 28"><line x1="16" y1="1" x2="2" y2="27" stroke="#ee834e" stroke-width="1.6"/></svg><span><b>Heading</b> Goes Here</span></div>
  <ul style="position:absolute;left:280px;top:125px;width:205px;list-style:none" class="lorem">
    <li style="margin-bottom:8px"><span class="orange">•</span>&nbsp; Lorem Ipsum Dolor Sit Amet, Consectetur Adipiscing Elit.</li>
    <li style="margin-bottom:8px"><span class="orange">•</span>&nbsp; Vivamus Eu Dui Ex. Curabitur Dapibus Dignissim Dui, In Molestie Metus Feugiat Sed.</li>
    <li style="margin-bottom:8px"><span class="orange">•</span>&nbsp; Praesent Aliquet Lorem Ex, Eu Dapibus Odio Varius At. Duis Eget Tellus Porta, Consequat Lacus Vitae, Venenatis Dolor.</li>
    <li><span class="orange">•</span>&nbsp; Nulla Facilisi. In Et Sollicitudin Lacus. Donec Risus Orci, Gravida Sit Amet Risus Vehicula, Aliquet Pretium Sapien.</li>
  </ul>
  <div class="footer"><span>Copyright © 2023 <b>Partwise Helm</b>. All Rights Reserved.</span><span class="page">2</span></div>
</section>

<!-- 3 About us -->
<section class="slide" style="left:51px;top:1108px" aria-label="About us slide">
  <div class="heading"><svg viewBox="0 0 18 28"><line x1="16" y1="1" x2="2" y2="27" stroke="#ee834e" stroke-width="1.6"/></svg><span style="font-weight:700;letter-spacing:.03em">ABOUT US</span></div>
  <div class="logo logo--corner">PARTWISE<br>HELM</div>
  <div class="photo photo--desk" role="img" aria-label="Photo of hands reviewing printed charts and a tablet on a desk" style="left:0;top:77px;width:540px;height:184px"></div>
  <div style="position:absolute;left:58px;top:77px;width:181px;height:184px;background:rgba(238,131,78,.92);color:#fff;text-align:center">
    <div class="circle" style="left:63px;top:16px;width:54px;height:54px;border:2px solid #fff">
      <svg viewBox="0 0 24 24"><rect x="3" y="7" width="18" height="13" rx="2" fill="#fff"/><rect x="9" y="4" width="6" height="4" rx="1" fill="none" stroke="#fff" stroke-width="1.6"/><line x1="8" y1="7" x2="8" y2="20" stroke="#ee834e" stroke-width="1.2"/><line x1="16" y1="7" x2="16" y2="20" stroke="#ee834e" stroke-width="1.2"/></svg>
    </div>
    <p style="position:absolute;left:14px;right:14px;top:82px;font-size:6px;line-height:1.25">Lorem Ipsum Dolor Sit Amet, Consectetur Adipiscing Elit. Vivamus Eu Dui Ex. Curabitur Dapibus Dignissim Dui, In Molestie Metus Feugiat Sed. Praesent Aliquet Lorem Ex, Eu Dapibus Odio Varius At. Duis Eget Tellus Porta, Consequat Lacus Vitae, Venenatis Dolor. Nulla Facilisi. In Et Sollicitudin Lacus. Donec Risus Orci, Gravida Sit Amet Risus Vehicula, Aliquet Pretium Sapien.</p>
  </div>
  <div class="footer"><span>Copyright © 2023 <b>Partwise Helm</b>. All Rights Reserved.</span><span class="page">3</span></div>
</section>

<!-- 4 Two column text + photo -->
<section class="slide" style="left:609px;top:1108px" aria-label="Feature slide">
  <div class="logo logo--corner">PARTWISE<br>HELM</div>
  <div class="heading" style="top:40px;align-items:flex-start"><svg viewBox="0 0 18 28"><line x1="16" y1="1" x2="2" y2="27" stroke="#ee834e" stroke-width="1.6"/></svg><span style="font-weight:700;line-height:1.2;font-size:16px">Vivamus Eu Dui Ex.<br>Curabitur Dapibus</span></div>
  <p class="lorem" style="position:absolute;left:65px;top:107px;width:195px">Lorem Ipsum Dolor Sit Amet, Consectetur Adipiscing Elit. Vivamus Eu Dui Ex. Curabitur Dapibus Dignissim Dui, In Molestie Metus Feugiat Sed. Praesent Aliquet Lorem Ex, Eu Dapibus Odio Varius At. Nulla Facilisi. In Et Sollicitudin Lacus.</p>
  <div class="circle" style="left:59px;top:165px;width:40px;height:40px;background:var(--orange)"><svg viewBox="0 0 24 24"><path d="M12 3a6 6 0 0 0-3.5 10.9V17h7v-3.1A6 6 0 0 0 12 3z" fill="#fff"/><rect x="9" y="18" width="6" height="2.5" rx="1" fill="#fff"/></svg></div>
  <p class="lorem" style="position:absolute;left:108px;top:168px;width:145px;font-size:4.8px">Lorem Ipsum Dolor Sit Amet, Consectetur Adipiscing Elit. Vivamus Eu Dui Ex. Curabitur Dapibus Dignissim Dui, In Molestie Metus Feugiat Sed. Praesent Aliquet Lorem Ex, Eu Dapibus Odio Varius At.</p>
  <div class="circle" style="left:59px;top:215px;width:40px;height:40px;background:var(--orange)"><svg viewBox="0 0 24 24"><circle cx="12" cy="12" r="7" fill="none" stroke="#fff" stroke-width="3" stroke-dasharray="3 2"/><circle cx="12" cy="12" r="3" fill="#fff"/></svg></div>
  <p class="lorem" style="position:absolute;left:108px;top:218px;width:145px;font-size:4.8px">Lorem Ipsum Dolor Sit Amet, Consectetur Adipiscing Elit. Vivamus Eu Dui Ex. Curabitur Dapibus Dignissim Dui, In Molestie Metus Feugiat Sed. Praesent Aliquet Lorem Ex, Eu Dapibus Odio Varius At.</p>
  <div class="photo photo--towers" role="img" aria-label="Photo looking up at glass skyscrapers" style="left:288px;top:44px;width:191px;height:159px"></div>
  <p class="lorem" style="position:absolute;left:293px;top:216px;width:190px;font-size:4.8px">Lorem Ipsum Dolor Sit Amet, Consectetur Adipiscing Elit. Vivamus Eu Dui Ex. Curabitur Dapibus Dignissim Dui, In Molestie Metus Feugiat Sed. Praesent Aliquet Lorem Ex, Eu Dapibus Odio Varius At. Nulla Facilisi. In Et Sollicitudin Lacus.</p>
  <div class="footer"><span>Copyright © 2023 <b>Partwise Helm</b>. All Rights Reserved.</span><span class="page">4</span></div>
</section>

<!-- 5 Icon grid -->
<section class="slide" style="left:51px;top:1430px" aria-label="Icon grid slide">
  <div class="heading"><svg viewBox="0 0 18 28"><line x1="16" y1="1" x2="2" y2="27" stroke="#ee834e" stroke-width="1.6"/></svg><span><b>Heading</b> Goes Here</span></div>
  <div class="logo logo--corner">PARTWISE<br>HELM</div>
  <div style="position:absolute;left:76px;top:88px;width:140px;text-align:right">
    <p style="font-size:8.5px;color:var(--navy)"><b style="font-weight:600">Title</b> Goes Here!</p>
    <p class="lorem" style="font-size:4.6px;margin-top:3px">Lorem Ipsum Dolor Sit Amet, Consectetur Adipiscing Elit. Vivamus Eu Dui Ex. Curabitur Dapibus Dignissim Dui, In Molestie Metus Feugiat Sed. Praesent Aliquet Lorem Ex.</p>
  </div>
  <div style="position:absolute;left:76px;top:144px;width:140px;text-align:right">
    <p style="font-size:8.5px;color:var(--navy)"><b style="font-weight:600">Title</b> Goes Here!</p>
    <p class="lorem" style="font-size:4.6px;margin-top:3px">Lorem Ipsum Dolor Sit Amet, Consectetur Adipiscing Elit. Vivamus Eu Dui Ex. Curabitur Dapibus Dignissim Dui, In Molestie Metus Feugiat Sed. Praesent Aliquet Lorem Ex.</p>
  </div>
  <div style="position:absolute;left:76px;top:200px;width:140px;text-align:right">
    <p style="font-size:8.5px;color:var(--navy)"><b style="font-weight:600">Title</b> Goes Here!</p>
    <p class="lorem" style="font-size:4.6px;margin-top:3px">Lorem Ipsum Dolor Sit Amet, Consectetur Adipiscing Elit. Vivamus Eu Dui Ex. Curabitur Dapibus Dignissim Dui, In Molestie Metus Feugiat Sed. Praesent Aliquet Lorem Ex.</p>
  </div>
  <div class="square" style="left:224px;top:90px;width:38px;height:38px"><svg viewBox="0 0 24 24"><circle cx="12" cy="12" r="8" fill="none" stroke="#fff" stroke-width="1.8"/><path d="M4 12h16M12 4c3 3 3 13 0 16M12 4c-3 3-3 13 0 16" fill="none" stroke="#fff" stroke-width="1.4"/></svg></div>
  <div class="square" style="left:278px;top:90px;width:38px;height:38px"><svg viewBox="0 0 24 24"><rect x="9" y="3" width="6" height="5" fill="#fff"/><rect x="3" y="16" width="5" height="5" fill="#fff"/><rect x="9.5" y="16" width="5" height="5" fill="#fff"/><rect x="16" y="16" width="5" height="5" fill="#fff"/><path d="M12 8v4M5.5 16v-4h13v4M12 12v4" fill="none" stroke="#fff" stroke-width="1.4"/></svg></div>
  <div class="square" style="left:224px;top:146px;width:38px;height:38px"><svg viewBox="0 0 24 24"><rect x="4" y="5" width="16" height="15" rx="1" fill="none" stroke="#fff" stroke-width="1.8"/><path d="M4 9h16M8 3v4M16 3v4" stroke="#fff" stroke-width="1.6"/><path d="M7 12h2M11 12h2M15 12h2M7 15h2M11 15h2M15 15h2" stroke="#fff" stroke-width="1.6"/></svg></div>
  <div class="square" style="left:278px;top:146px;width:38px;height:38px"><svg viewBox="0 0 24 24"><path d="M11 4a8 8 0 1 0 8 8h-8z" fill="#fff"/><path d="M13 2v8h8a8 8 0 0 0-8-8z" fill="#fff"/></svg></div>
  <div class="square" style="left:224px;top:202px;width:38px;height:38px"><svg viewBox="0 0 24 24"><path d="M6 3h9l4 4v14H6z" fill="#fff"/><path d="M9 10h7M9 13h7M9 16h5" stroke="#ee834e" stroke-width="1.3"/></svg></div>
  <div class="square" style="left:278px;top:202px;width:38px;height:38px"><svg viewBox="0 0 24 24"><text x="12" y="19" text-anchor="middle" font-family="Open Sans,Arial,sans-serif" font-weight="800" font-size="19" fill="#fff">$</text></svg></div>
  <div style="position:absolute;left:334px;top:87px;width:145px">
    <p style="font-size:8.5px;color:var(--navy)"><b style="font-weight:600">Title</b> Goes Here!</p>
    <p class="lorem" style="font-size:4.6px;margin-top:3px">Lorem Ipsum Dolor Sit Amet, Consectetur Adipiscing Elit. Vivamus Eu Dui Ex. Curabitur Dapibus Dignissim Dui, In Molestie Metus Feugiat Sed. Praesent Aliquet Lorem Ex.</p>
  </div>
  <div style="position:absolute;left:334px;top:143px;width:145px">
    <p style="font-size:8.5px;color:var(--navy)"><b style="font-weight:600">Title</b> Goes Here!</p>
    <p class="lorem" style="font-size:4.6px;margin-top:3px">Lorem Ipsum Dolor Sit Amet, Consectetur Adipiscing Elit. Vivamus Eu Dui Ex. Curabitur Dapibus Dignissim Dui, In Molestie Metus Feugiat Sed. Praesent Aliquet Lorem Ex.</p>
  </div>
  <div style="position:absolute;left:334px;top:199px;width:145px">
    <p style="font-size:8.5px;color:var(--navy)"><b style="font-weight:600">Title</b> Goes Here!</p>
    <p class="lorem" style="font-size:4.6px;margin-top:3px">Lorem Ipsum Dolor Sit Amet, Consectetur Adipiscing Elit. Vivamus Eu Dui Ex. Curabitur Dapibus Dignissim Dui, In Molestie Metus Feugiat Sed. Praesent Aliquet Lorem Ex.</p>
  </div>
  <div class="footer"><span>Copyright © 2023 <b>Partwise Helm</b>. All Rights Reserved.</span><span class="page">5</span></div>
</section>

<!-- 6 Three columns -->
<section class="slide" style="left:609px;top:1430px" aria-label="Three column slide">
  <div class="heading"><svg viewBox="0 0 18 28"><line x1="16" y1="1" x2="2" y2="27" stroke="#ee834e" stroke-width="1.6"/></svg><span><b>Heading</b> Goes Here</span></div>
  <div class="logo logo--corner">PARTWISE<br>HELM</div>
  <div style="position:absolute;left:17px;top:80px;width:161px;text-align:center">
    <p style="font-size:8.5px;color:var(--orange)"><b style="font-weight:600">Title</b> Goes Here!</p>
    <div class="photo photo--chart" role="img" aria-label="Photo of a hand with a pen over printed charts" style="position:relative;height:93px;margin-top:6px"></div>
    <p class="lorem" style="margin-top:10px;font-size:5.6px">Lorem ipsum dolor sit amet, at laborum nibh duis mauris. Per ultrices lectus sed metus tristique eu. Diam suspendisse ac ipsum maecenas.</p>
  </div>
  <div style="position:absolute;left:190px;top:80px;width:160px;text-align:center">
    <p style="font-size:8.5px;color:var(--orange)"><b style="font-weight:600">Title</b> Goes Here!</p>
    <div class="photo photo--meeting" role="img" aria-label="Photo of a handshake over a tablet showing a chart" style="position:relative;height:93px;margin-top:6px"></div>
    <p class="lorem" style="margin-top:10px;font-size:5.6px">Lorem ipsum dolor sit amet, at laborum nibh duis mauris. Per ultrices lectus sed metus tristique eu. Diam suspendisse ac ipsum maecenas.</p>
  </div>
  <div style="position:absolute;left:362px;top:80px;width:161px;text-align:center">
    <p style="font-size:8.5px;color:var(--orange)"><b style="font-weight:600">Title</b> Goes Here!</p>
    <div class="photo photo--towers" role="img" aria-label="Photo looking up at glass skyscrapers" style="position:relative;height:93px;margin-top:6px"></div>
    <p class="lorem" style="margin-top:10px;font-size:5.6px">Lorem ipsum dolor sit amet, at laborum nibh duis mauris. Per ultrices lectus sed metus tristique eu. Diam suspendisse ac ipsum maecenas.</p>
  </div>
  <div class="footer"><span>Copyright © 2023 <b>Partwise Helm</b>. All Rights Reserved.</span><span class="page">6</span></div>
</section>

<!-- 7 Centre band -->
<section class="slide" style="left:51px;top:1752px" aria-label="Four point slide">
  <div class="photo" role="img" aria-label="Faint photo of skyscrapers tinted orange" style="left:181px;top:0;width:177px;height:304px;background:linear-gradient(180deg,#f09462 0%,#ee834e 55%,#e97a44 100%)"></div>
  <p style="position:absolute;left:181px;width:177px;top:128px;text-align:center;color:#fff;font-size:16px;line-height:1.2"><b>Heading</b><br>Goes Here</p>
  <div class="logo logo--corner">PARTWISE<br>HELM</div>
  <div class="circle" style="left:158px;top:60px;width:46px;height:46px;background:#111;border:2px solid #fff"><svg viewBox="0 0 24 24"><path d="M12 3a6 6 0 0 0-3.5 10.9V17h7v-3.1A6 6 0 0 0 12 3z" fill="#fff"/><rect x="9" y="18" width="6" height="2.5" rx="1" fill="#fff"/></svg></div>
  <div class="circle" style="left:158px;top:170px;width:46px;height:46px;background:#111;border:2px solid #fff"><svg viewBox="0 0 24 24"><circle cx="12" cy="8" r="3" fill="#fff"/><circle cx="5.5" cy="10" r="2.3" fill="#fff"/><circle cx="18.5" cy="10" r="2.3" fill="#fff"/><path d="M6 19a6 6 0 0 1 12 0z" fill="#fff"/><path d="M1 18a4.5 4.5 0 0 1 6-3.5M23 18a4.5 4.5 0 0 0-6-3.5" fill="none" stroke="#fff" stroke-width="1.8"/></svg></div>
  <div class="circle" style="left:335px;top:60px;width:46px;height:46px;background:#111;border:2px solid #fff"><svg viewBox="0 0 24 24"><circle cx="10" cy="10" r="6" fill="none" stroke="#fff" stroke-width="2.4"/><line x1="14.5" y1="14.5" x2="20" y2="20" stroke="#fff" stroke-width="3"/></svg></div>
  <div class="circle" style="left:335px;top:170px;width:46px;height:46px;background:#111;border:2px solid #fff"><svg viewBox="0 0 24 24"><rect x="4" y="15" width="3" height="5" fill="#fff"/><rect x="9" y="12" width="3" height="8" fill="#fff"/><rect x="14" y="9" width="3" height="11" fill="#fff"/><path d="M4 12l6-5 3 3 6-6M15 4h4v4" fill="none" stroke="#fff" stroke-width="1.6"/></svg></div>
  <div style="position:absolute;left:20px;top:62px;width:132px;text-align:right">
    <p style="font-size:8.5px;color:var(--orange);line-height:1.15"><b>Vivamus Eu Dui Ex.</b><br>Curabitur Dapibus</p>
    <p class="lorem" style="font-size:4.8px;margin-top:6px">Lorem Ipsum Dolor Sit Amet, Consectetur Adipiscing Elit. Vivamus Eu Dui Ex. Curabitur Dapibus Dignissim Dui, In Molestie Metus Feugiat Sed. Praesent Aliquet Lorem Ex, Eu Dapibus Odio Varius At. Nulla Facilisi.</p>
  </div>
  <div style="position:absolute;left:20px;top:172px;width:132px;text-align:right">
    <p style="font-size:8.5px;color:var(--orange);line-height:1.15"><b>Vivamus Eu Dui Ex.</b><br>Curabitur Dapibus</p>
    <p class="lorem" style="font-size:4.8px;margin-top:6px">Lorem Ipsum Dolor Sit Amet, Consectetur Adipiscing Elit. Vivamus Eu Dui Ex. Curabitur Dapibus Dignissim Dui, In Molestie Metus Feugiat Sed. Praesent Aliquet Lorem Ex, Eu Dapibus Odio Varius At. Nulla Facilisi.</p>
  </div>
  <div style="position:absolute;left:392px;top:62px;width:122px">
    <p style="font-size:8.5px;color:var(--orange);line-height:1.15"><b>Vivamus Eu Dui Ex.</b><br>Curabitur Dapibus</p>
    <p class="lorem" style="font-size:4.8px;margin-top:6px">Lorem Ipsum Dolor Sit Amet, Consectetur Adipiscing Elit. Vivamus Eu Dui Ex. Curabitur Dapibus Dignissim Dui, In Molestie Metus Feugiat Sed. Praesent Aliquet Lorem Ex, Eu Dapibus Odio Varius At. Nulla Facilisi.</p>
  </div>
  <div style="position:absolute;left:392px;top:172px;width:122px">
    <p style="font-size:8.5px;color:var(--orange);line-height:1.15"><b>Vivamus Eu Dui Ex.</b><br>Curabitur Dapibus</p>
    <p class="lorem" style="font-size:4.8px;margin-top:6px">Lorem Ipsum Dolor Sit Amet, Consectetur Adipiscing Elit. Vivamus Eu Dui Ex. Curabitur Dapibus Dignissim Dui, In Molestie Metus Feugiat Sed. Praesent Aliquet Lorem Ex, Eu Dapibus Odio Varius At. Nulla Facilisi.</p>
  </div>
  <div class="footer"><span>Copyright © 2023 <b>Partwise Helm</b>. All Rights Reserved.</span><span class="page">7</span></div>
</section>

<!-- 8 Chart -->
<section class="slide" style="left:609px;top:1752px" aria-label="Chart slide">
  <div class="heading"><svg viewBox="0 0 18 28"><line x1="16" y1="1" x2="2" y2="27" stroke="#ee834e" stroke-width="1.6"/></svg><span><b>Heading</b> Goes Here</span></div>
  <div class="logo logo--corner">PARTWISE<br>HELM</div>
  <svg class="bar-chart" style="position:absolute;left:44px;top:90px" width="225" height="145" viewBox="0 0 225 145" font-family="Open Sans,Arial,sans-serif" font-size="4.5" fill="#555">
    <g text-anchor="end">
      <text x="8" y="130">0</text><text x="8" y="109.3">1</text><text x="8" y="88.7">2</text><text x="8" y="68">3</text><text x="8" y="47.3">4</text><text x="8" y="26.7">5</text><text x="8" y="6">6</text>
    </g>
    <line x1="12" y1="128" x2="218" y2="128" stroke="#ccc" stroke-width=".6"/>
    <g>
      <rect x="19" y="39.1" width="7" height="88.9" fill="#ee834e"/><rect x="27" y="78.4" width="7" height="49.6" fill="#a6a6a6"/><rect x="35" y="86.7" width="7" height="41.3" fill="#111"/>
      <rect x="53" y="76.3" width="7" height="51.7" fill="#ee834e"/><rect x="61" y="39.1" width="7" height="88.9" fill="#a6a6a6"/><rect x="69" y="86.7" width="7" height="41.3" fill="#111"/>
      <rect x="87" y="55.7" width="7" height="72.3" fill="#ee834e"/><rect x="95" y="90.8" width="7" height="37.2" fill="#a6a6a6"/><rect x="103" y="66" width="7" height="62" fill="#111"/>
      <rect x="121" y="35" width="7" height="93" fill="#ee834e"/><rect x="129" y="70.1" width="7" height="57.9" fill="#a6a6a6"/><rect x="137" y="24.6" width="7" height="103.4" fill="#111"/>
      <rect x="155" y="39.1" width="7" height="88.9" fill="#ee834e"/><rect x="163" y="78.4" width="7" height="49.6" fill="#a6a6a6"/><rect x="171" y="86.7" width="7" height="41.3" fill="#111"/>
      <rect x="189" y="76.3" width="7" height="51.7" fill="#ee834e"/><rect x="197" y="39.1" width="7" height="88.9" fill="#a6a6a6"/><rect x="205" y="86.7" width="7" height="41.3" fill="#111"/>
    </g>
    <g text-anchor="middle" font-size="4">
      <text x="30" y="137">Category 1</text><text x="64" y="137">Category 2</text><text x="98" y="137">Category 3</text><text x="132" y="137">Category 4</text><text x="166" y="137">Category 5</text><text x="200" y="137">Category 6</text>
    </g>
  </svg>
  <div class="circle" style="left:277px;top:90px;width:40px;height:40px;background:var(--orange)"><svg viewBox="0 0 24 24"><circle cx="12" cy="8" r="4" fill="#fff"/><path d="M4 21a8 8 0 0 1 16 0z" fill="#fff"/></svg></div>
  <p class="lorem" style="position:absolute;left:324px;top:92px;width:180px;font-size:4.9px">Lorem ipsum dolor sit amet, at laborum nibh duis mauris. Per ultrices lectus sed metus tristique eu. Diam suspendisse ac ipsum maecenas fermentum, aliquet imperdiet et lobortis venenatis nascetur lacus. A ac, vivamus erat nullam.</p>
  <div class="circle" style="left:277px;top:144px;width:40px;height:40px;background:var(--navy)"><svg viewBox="0 0 24 24"><path d="M8 3v18M16 3v18" stroke="#fff" stroke-width="2.4"/><path d="M5 4h6M13 8h6" stroke="#fff" stroke-width="2"/></svg></div>
  <p class="lorem" style="position:absolute;left:324px;top:146px;width:180px;font-size:4.9px">Lorem ipsum dolor sit amet, at laborum nibh duis mauris. Per ultrices lectus sed metus tristique eu. Diam suspendisse ac ipsum maecenas fermentum, aliquet imperdiet et lobortis venenatis nascetur lacus. A ac, vivamus erat nullam.</p>
  <div class="circle" style="left:277px;top:198px;width:40px;height:40px;background:#8f8f8f"><svg viewBox="0 0 24 24"><rect x="3" y="10" width="4" height="10" fill="#fff"/><path d="M9 10l4-7c2 0 2.5 1.5 2 4h5c1.2 0 1.8 1 1.5 2l-2 9c-.2.6-.8 1-1.5 1H9z" fill="#fff"/></svg></div>
  <p class="lorem" style="position:absolute;left:324px;top:200px;width:180px;font-size:4.9px">Lorem ipsum dolor sit amet, at laborum nibh duis mauris. Per ultrices lectus sed metus tristique eu. Diam suspendisse ac ipsum maecenas fermentum, aliquet imperdiet et lobortis venenatis nascetur lacus. A ac, vivamus erat nullam.</p>
  <div class="footer"><span>Copyright © 2023 <b>Partwise Helm</b>. All Rights Reserved.</span><span class="page">8</span></div>
</section>

<!-- 9 Table -->
<section class="slide" style="left:51px;top:2074px" aria-label="Table slide">
  <div class="heading"><svg viewBox="0 0 18 28"><line x1="16" y1="1" x2="2" y2="27" stroke="#ee834e" stroke-width="1.6"/></svg><span><b>Heading</b> Goes Here</span></div>
  <div class="logo logo--corner">PARTWISE<br>HELM</div>
  <table class="data-table" style="position:absolute;left:27px;top:76px;width:486px;border-collapse:collapse;font-size:5.4px;color:var(--navy)">
    <thead>
      <tr style="height:24px;color:#fff;font-weight:700">
        <th style="background:#555;text-align:left;padding-left:4px;width:150px">Heading Goes Here</th>
        <th style="background:var(--orange);line-height:1.2">Heading<br>Goes Here</th>
        <th style="background:#a6a6a6;line-height:1.2">Heading<br>Goes Here</th>
        <th style="background:#a6a6a6;line-height:1.2">Heading<br>Goes Here</th>
        <th style="background:#a6a6a6;line-height:1.2">Heading<br>Goes Here</th>
      </tr>
    </thead>
    <tbody style="text-align:center">
      <tr style="height:22px"><td style="text-align:left;padding-left:4px;font-weight:700">Lorem ipsum dolor sit amet</td><td>23</td><td>12</td><td>78</td><td>78</td></tr>
      <tr style="height:22px;background:var(--light)"><td style="text-align:left;padding-left:4px;font-weight:700">Vivamus eu dui ex. Curabitur dapibus</td><td>45</td><td>56</td><td>12</td><td>76</td></tr>
      <tr style="height:22px"><td style="text-align:left;padding-left:4px;font-weight:700">Praesent aliquet lorem ex, eu dapibus</td><td>78</td><td>76</td><td>34</td><td>34</td></tr>
      <tr style="height:22px;background:var(--light)"><td style="text-align:left;padding-left:4px;font-weight:700">Duis eget tellus porta, consequat lacus</td><td>22</td><td>12</td><td>55</td><td>67</td></tr>
      <tr style="height:22px"><td style="text-align:left;padding-left:4px;font-weight:700">Donec risus orci, gravida sit amet</td><td>34</td><td>66</td><td>45</td><td>11</td></tr>
      <tr style="height:22px;background:var(--light)"><td style="text-align:left;padding-left:4px;font-weight:700">Nunc placerat, arcu nec mattis</td><td>67</td><td>47</td><td>78</td><td>23</td></tr>
      <tr style="height:22px"><td style="text-align:left;padding-left:4px;font-weight:700">Nam semper tristique mauris</td><td>87</td><td>67</td><td>12</td><td>45</td></tr>
    </tbody>
  </table>
  <div class="footer"><span>Copyright © 2023 <b>Partwise Helm</b>. All Rights Reserved.</span><span class="page">9</span></div>
</section>

<!-- 10 Contact -->
<section class="slide" style="left:609px;top:2074px" aria-label="Contact slide">
  <div class="photo photo--towers" role="img" aria-label="Photo looking up at glass skyscrapers" style="inset:0;clip-path:polygon(235px 0,540px 0,540px 304px,20px 304px);opacity:.95"></div>
  <div style="position:absolute;inset:0;background:linear-gradient(90deg,#fff 30%,rgba(255,255,255,0) 60%)"></div>
  <svg style="position:absolute;inset:0" width="540" height="304"><polygon points="446,0 462,0 256,304 240,304" fill="#ee834e"/></svg>
  <div class="logo logo--large" style="left:45px;top:45px">PARTWISE<br>HELM</div>
  <p style="position:absolute;left:45px;top:163px;font-size:9.5px;font-weight:700;color:var(--navy)">Contact Us</p>
  <ul style="position:absolute;left:45px;top:186px;list-style:none;font-size:6.2px;color:var(--navy)">
    <li style="display:flex;align-items:center;gap:6px;height:16px"><svg width="9" height="9" viewBox="0 0 24 24"><path d="M6 3l3 4-2 2.5a12 12 0 0 0 7.5 7.5L17 15l4 3-1.5 3c-9 0-17-8-17-17z" fill="none" stroke="#ee834e" stroke-width="2"/></svg>Phone Number Goes Here</li>
    <li style="display:flex;align-items:center;gap:6px;height:16px"><svg width="9" height="9" viewBox="0 0 24 24"><circle cx="12" cy="12" r="4" fill="none" stroke="#ee834e" stroke-width="2"/><path d="M16 12v2a3 3 0 0 0 6 0v-2a10 10 0 1 0-4 8" fill="none" stroke="#ee834e" stroke-width="2"/></svg>E-Mail Address Goes Here</li>
    <li style="display:flex;align-items:center;gap:6px;height:16px"><svg width="9" height="9" viewBox="0 0 24 24"><circle cx="12" cy="12" r="9" fill="none" stroke="#ee834e" stroke-width="2"/><path d="M3 12h18M12 3c4 4 4 14 0 18M12 3c-4 4-4 14 0 18" fill="none" stroke="#ee834e" stroke-width="1.5"/></svg>URL Address Goes Here</li>
  </ul>
  <p style="position:absolute;left:45px;top:255px;font-size:4.2px;color:var(--navy)">Copyright © 2023 Partwise Helm. All Rights Reserved.</p>
</section>

</body>
</html>
```